Business card design Needed for new logo / Construction business, home extensions and new builds

We need a business card design using our new logo files which i will attach to this project :)

We are a small construction business specialising in home extensions, new builds and property development. We are very ambitious and would appreciate professional and elegant designs for our new business card.

Very serious about using the services on BriefNest and recently acquired our new logo from here :)

Please get involved, i will feedback when i can as i am very busy but can respond daily, thanks

Target Market(s)

People that want to build onto their houses, new building developments or adding too their existing property

Industry/Entity Type

Construction

Contact Information for Business Card

Hollin Marsh Construction, Tobias Renwick (Managing Director), Tel 07822200444, email - info@hollin-marsh, www.hollin-marsh.co.uk

Colors

Designer to choose colors to be used in the design.

Requirements
Must have
• I like a deep grey on the back please. A lot of you have provided black from and back, try mixing things up a little. The black looks cool 😎 Thanks

```html
<!DOCTYPE html>
<html lang="en">
<head>
<meta charset="utf-8">
<title>Hollin Marsh Construction – Business Card</title>
<link href="https://fonts.googleapis.com/css2?family=Cinzel:wght@400;600&family=Poppins:wght@400;500&display=swap" rel="stylesheet">
<style>
  :root {
    --backdrop: #3a3a3a;
    --card-black: #141414;
    --card-front: #1b1b1b;
    --silver: #d6d6d6;
    --gold: #d9a521;
    --ink-light: #ececec;
    --pattern-dark: #1e1e1e;
    --pattern-light: #2c2c2c;
  }
  * { box-sizing: border-box; margin: 0; padding: 0; }
  html, body { width: 1200px; height: 959px; overflow: hidden; }
  body {
    background: var(--backdrop);
    position: relative;
    font-family: "Poppins", sans-serif;
  }
  .card {
    position: absolute;
    left: 250px;
    width: 700px;
    height: 400px;
    overflow: hidden;
    box-shadow: 0 12px 30px rgba(0,0,0,.45);
  }
  .card--back { top: 53px; background: var(--card-black); }
  .card--front { top: 506px; background: var(--card-front); }

  .pattern-field {
    position: absolute; inset: 0;
    background: linear-gradient(135deg, var(--pattern-light), var(--pattern-dark) 60%, #111);
    opacity: .9;
  }
  .brand {
    position: absolute;
    display: flex; align-items: center; gap: 14px;
  }
  .brand__square {
    width: 30px; height: 30px;
    background: var(--gold);
    flex: none;
  }
  .brand__name {
    font-family: "Cinzel", serif;
    font-weight: 600;
    color: var(--silver);
    letter-spacing: .06em;
    line-height: 1.15;
  }
  .card--back .brand {
    left: 50%; top: 50%;
    transform: translate(-50%, -50%);
  }
  .card--back .brand__name { font-size: 30px; }

  .front-mark {
    position: absolute; right: 0; top: 0;
    width: 300px; height: 400px;
    background: linear-gradient(160deg, #242424, #161616 70%);
  }
  .front-info { position: absolute; left: 56px; top: 48px; }
  .card--front .brand { position: static; }
  .card--front .brand__name { font-size: 24px; }
  .person { margin-top: 40px; }
  .person__name {
    font-family: "Cinzel", serif;
    font-size: 24px;
    color: var(--silver);
    letter-spacing: .04em;
  }
  .person__role {
    font-size: 15px;
    color: var(--gold);
    margin-top: 2px;
  }
  .contacts { list-style: none; margin-top: 34px; }
  .contacts li {
    display: flex; align-items: center; gap: 12px;
    font-size: 16px;
    color: var(--ink-light);
    margin-bottom: 10px;
  }
  .contacts svg { width: 16px; height: 16px; flex: none; }
</style>
</head>
<body>
  <section class="card card--back">
    <div class="pattern-field" role="img" aria-label="Repeating tone-on-tone pattern of the company emblem"></div>
    <div class="brand">
      <span class="brand__square"></span>
      <span class="brand__name">Hollin Marsh Construction</span>
    </div>
  </section>

  <section class="card card--front">
    <div class="front-mark" role="img" aria-label="Large embossed company emblem in dark tones"></div>
    <div class="front-info">
      <div class="brand">
        <span class="brand__square"></span>
        <span class="brand__name">Hollin Marsh Construction</span>
      </div>
      <div class="person">
        <p class="person__name">Tobias Renwick</p>
        <p class="person__role">Managing Director</p>
      </div>
      <ul class="contacts">
        <li>
          <svg viewBox="0 0 16 16" aria-hidden="true"><path d="M3 1.5l2.5 3-1.5 1.8c.9 2 2.6 3.7 4.7 4.7L10.5 9.5l3 2.5-1.4 2.5C6.8 14.3 1.7 9.2 1.5 3.9z" fill="var(--gold)"/></svg>
          07822200444
        </li>
        <li>
          <svg viewBox="0 0 16 16" aria-hidden="true"><rect x="1" y="3" width="14" height="10" fill="none" stroke="var(--gold)" stroke-width="1.6"/><path d="M1 3l7 5.5L15 3" fill="none" stroke="var(--gold)" stroke-width="1.6"/></svg>
          info@hollin-marsh
        </li>
        <li>
          <svg viewBox="0 0 16 16" aria-hidden="true"><circle cx="8" cy="8" r="6.5" fill="none" stroke="var(--gold)" stroke-width="1.4"/><ellipse cx="8" cy="8" rx="3" ry="6.5" fill="none" stroke="var(--gold)" stroke-width="1.2"/><path d="M1.5 8h13M2.5 5h11M2.5 11h11" stroke="var(--gold)" stroke-width="1"/></svg>
          www.hollin-marsh.co.uk
        </li>
      </ul>
    </div>
  </section>
</body>
</html>
```